Traineeship Flyer Design Project

Requirements:
• 1 x A4 page flyer (double sided)
1st page; target market 15-19 yr old, looking for young/fresh, exciting, eye catching
2nd page: same look/feel – target market – parents/person to determine if there is value to devoting energy to this qualification (potentially less busy in design)
• Use of high quality logos: 1. Quandrel 2. Nationally recognised training logo
Ideally wanting to keep amount of copy to the page layout as attached, although designer is free to interpret the layout of copy on each page, although Quandrel will accept alternative presentation if designer sees new way to combine information
• Quandrel does not have a set colour palette so there are no restrictions/guidelines to follow
Updates
Hi, All files including brief and logos have now been updated.
Reason: Hi everyone
Please refer to design submission below for the only design that was deemed to cover off on the brief as the starting point - in regards to producing a design that appeals to target market of young person (15-19) in regards to self selecting to take up further study
Hi everyone
Can you please view the 3 remaining designs that are in contention (out of 30+ submitted) - Design 1528020 ; 1510098; 1510087; I will be providing additional feedback to these designers, as that come closer to the mark of appealing to younger "potential trainee" - the collateral needs to make the young student want to pick up the flyer (eye catching/interesting) and then be motivated to want to self elect - "beg parents" to take up the option. **PLEASE NOTE - I have uploaded a colour swatch now, and would appreciate if desgins could use these colours (not a requirement to use base colours of blue a silver as base if an exciting image needs to come from leaning on "secondary colours" (brighter) as being the predominant colours.
Many thanks, appreciate being able to see such an active community of designers involved in this website
Target Market(s)
1st page; target market 15-19 yr old, looking for young/fresh, exciting, eye catching. same look/feel – target market – parents/person to decide on
Industry/Entity Type
Training
Look and feel

```html
<!DOCTYPE html>
<html lang="en">
<head>
<meta charset="utf-8">
<title>Quandrel National Traineeships</title>
<link rel="stylesheet" href="https://fonts.googleapis.com/css2?family=Oswald:wght@500&family=Roboto+Condensed:wght@400&family=Arimo:wght@400;700&family=Archivo+Narrow:wght@700&display=swap">
<style>
  :root {
    --paper: #f1e8d8;
    --tan: #c9b496;
    --ink: #2f2a22;
    --dark: #3a342a;
    --band-1: #3a342a;
    --band-2: #a3391f;
    --band-3: #e0262a;
    --band-4: #ea5a27;
    --band-5: #ef7f24;
    --band-6: #f4a126;
    --accent: #ec6c23;
    --chev-1: #b8443a;
    --chev-2: #8daf48;
    --chev-3: #7b4f99;
    --chev-4: #3fa4b5;
    --logo-grey: #8c8c8c;
  }
  * { box-sizing: border-box; margin: 0; padding: 0; }
  html, body { width: 848px; height: 1200px; overflow: hidden; }
  body {
    background: var(--paper);
    font-family: "Arimo", Arial, sans-serif;
    color: var(--ink);
    position: relative;
  }
  .edge { position: absolute; left: 0; width: 848px; }
  .edge--top-dark { top: 0; height: 7px; background: var(--dark); }
  .edge--top-tan { top: 7px; height: 14px; background: var(--tan); }
  .edge--bottom-tan { top: 1168px; height: 18px; background: var(--tan); }
  .edge--bottom-dark { top: 1186px; height: 14px; background: var(--dark); }

  .brand {
    position: absolute; left: 50px; top: 80px;
    display: flex; align-items: center; gap: 10px;
    font-family: "Arimo", Arial, sans-serif; font-size: 32px; font-weight: 400;
    color: var(--logo-grey);
  }
  .brand__mark { width: 30px; height: 30px; background: var(--logo-grey); }

  .masthead { position: absolute; left: 0; top: 0; }
  .masthead__title {
    font-family: "Oswald", "Arial Narrow", sans-serif; font-weight: 500;
    font-size: 48px; fill: #fff;
  }

  .taglines {
    position: absolute; left: 54px; top: 184px;
    font-size: 21px; font-weight: 700; color: var(--accent); line-height: 30px;
  }

  .steps { position: absolute; left: 0; top: 0; }
  .steps__label {
    font-family: "Roboto Condensed", "Arial Narrow", sans-serif;
    font-size: 33px; fill: #fff;
  }

  .copy { position: absolute; left: 54px; width: 760px; }
  .copy__lead {
    top: 634px; font-size: 21px; font-weight: 700; color: var(--accent); line-height: 27px;
  }
  .copy__q { font-family: "Archivo Narrow", "Arial Narrow", sans-serif; font-size: 14px; font-weight: 700; }
  .copy__p { font-size: 13.5px; line-height: 19px; }

  .faq-cost { top: 700px; }
  .faq-cost .copy__p { margin: 6px 0 2px; }

  .duties { position: absolute; left: 54px; top: 770px; list-style: none; }
  .duties li { font-size: 13.5px; line-height: 22px; padding-left: 26px; position: relative; }
  .duties li::before {
    content: ""; position: absolute; left: 4px; top: 8px;
    width: 6px; height: 6px; border-radius: 50%; background: var(--ink);
  }
  .duties__brace { position: absolute; left: 306px; top: 770px; }
  .duties__note {
    position: absolute; left: 336px; top: 810px;
    font-size: 20px; font-weight: 700; color: var(--accent);
  }

  .faq-length { top: 884px; }
  .faq-length .copy__p { margin-top: 8px; }

  .copy__signup {
    top: 978px; font-size: 21px; font-weight: 700; color: var(--accent); line-height: 27px;
  }

  .pathway { position: absolute; left: 28px; top: 1054px; }
  .pathway__text { font-family: "Arimo", Arial, sans-serif; font-size: 12px; fill: #fff; }
  .pathway__code { fill: rgba(255,255,255,0.75); }
</style>
</head>
<body>
  <div class="edge edge--top-dark"></div>
  <div class="edge edge--top-tan"></div>

  <div class="brand"><span class="brand__mark"></span>Quandrel</div>

  <svg class="masthead" width="848" height="160" viewBox="0 0 848 160">
    <polygon points="266,64 300,64 250,150 216,150" fill="var(--dark)"/>
    <polygon points="316,64 848,64 848,150 266,150" fill="var(--dark)"/>
    <text class="masthead__title" x="374" y="125" textLength="458" lengthAdjust="spacingAndGlyphs">NATIONAL TRAINEESHIPS</text>
  </svg>

  <div class="taglines">
    <p>Kick-start your career today for free!</p>
    <p>Get ahead of the game</p>
    <p>Learn on the job</p>
  </div>

  <svg class="steps" width="848" height="640" viewBox="0 0 848 640">
    <polygon points="0,313 848,241 848,292 0,364" fill="var(--band-1)"/>
    <polygon points="0,364 848,292 848,342 0,414" fill="var(--band-2)"/>
    <polygon points="0,414 848,342 848,393 0,465" fill="var(--band-3)"/>
    <polygon points="0,465 848,393 848,443 0,515" fill="var(--band-4)"/>
    <polygon points="0,515 848,443 848,494 0,566" fill="var(--band-5)"/>
    <polygon points="0,566 848,494 848,544 0,616" fill="var(--band-6)"/>
    <g transform="rotate(-4.8 54 349)">
      <text class="steps__label" x="54" y="349">Step 1 – Information session</text>
      <text class="steps__label" x="54" y="400">Step 2 – Register your interest</text>
      <text class="steps__label" x="54" y="450">Step 3 - Enrolment</text>
      <text class="steps__label" x="54" y="501">Step 4 – Start training</text>
      <text class="steps__label" x="54" y="551">Step 5 – Practical assessments</text>
      <text class="steps__label" x="54" y="602">Step 6 - Graduate</text>
    </g>
  </svg>

  <p class="copy copy__lead">Gain a formal national qualification recognised by all employers Australia wide.</p>

  <div class="copy faq-cost">
    <p class="copy__q">How much will it cost?</p>
    <p class="copy__p">Nothing! The full course is provided by your employer. No prior training/experience is required</p>
    <p class="copy__q">What would I be expected to do?</p>
  </div>

  <ul class="duties">
    <li>Earn while your learn</li>
    <li>Attend on site training sessions</li>
    <li>Online training and assessment</li>
    <li>Complete workplace activities</li>
  </ul>
  <svg class="duties__brace" width="24" height="92" viewBox="0 0 24 92">
    <path d="M3,3 Q12,3 12,14 L12,38 Q12,46 20,46 Q12,46 12,54 L12,78 Q12,89 3,89" fill="none" stroke="var(--ink)" stroke-width="2.5"/>
  </svg>
  <p class="duties__note">All training completed during paid work time</p>

  <div class="copy faq-length">
    <p class="copy__q">How long will it take to finish my traineeship?</p>
    <p class="copy__p">If you remain on track, you could complete a Cert II in 6 months or a Cert III in 7 months. Don’t worry, a dedicated Trainer is committed to making your training a fun, informative and worthwhile experience.</p>
  </div>

  <p class="copy copy__signup">Sign up today for the opportunity to complete one of these qualifications</p>

  <svg class="pathway" width="800" height="74" viewBox="0 0 800 74">
    <polygon points="0,0 180,0 205,37 180,74 0,74 18,37" fill="var(--chev-1)"/>
    <polygon points="196,0 380,0 405,37 380,74 196,74 221,37" fill="var(--chev-2)"/>
    <polygon points="396,0 580,0 605,37 580,74 396,74 421,37" fill="var(--chev-3)"/>
    <polygon points="596,0 775,0 800,37 775,74 596,74 621,37" fill="var(--chev-4)"/>
    <g class="pathway__text" text-anchor="middle">
      <text x="105" y="24">Certificate II</text>
      <text x="105" y="42">Retail Services</text>
      <text class="pathway__code" x="105" y="60">(SIR20212)</text>
      <text x="302" y="24">Certificate III</text>
      <text x="302" y="42">Retail Operations</text>
      <text class="pathway__code" x="302" y="60">(SIR30212)</text>
      <text x="502" y="24">Certificate IV</text>
      <text x="502" y="42">Frontline Management</text>
      <text class="pathway__code" x="502" y="60">(BSB40807)</text>
      <text x="700" y="28">Diploma in</text>
      <text x="700" y="45">Business</text>
      <text class="pathway__code" x="700" y="62">(SIR50107)</text>
    </g>
  </svg>

  <div class="edge edge--bottom-tan"></div>
  <div class="edge edge--bottom-dark"></div>
</body>
</html>
```